Electrical contractor

looking for a standard sized, horizontal, double sided business card for an electrical contractors business.
i have played around on microsoft word (only computer program i know how to use!) and will attach what i have made so far, really open to any ideas. i just want the DORB to stand out to the rest of the business name.

i wish to use the colours black and green, and white for writing. i will attach the pictures i took off google, i want to either use them, or somethin similar for the back grounds

i wish the front to have the following info:
business name: D.O.R.B ELECTRICAL CONTRACTORS
MY NAME; CORBIN HOLT
STATUS; A CLASS ELECTRICIAN
LICENSE NO; TRN517394
PH NO. 0431576204
EMAIL ADD. DORB.ELECTRICAL@VELTOMAIL.COM
AND MY SLOGAN: where excellence meets integrity, and service comes with a smile.

i am not sure what to have on the back, other than what i do for work.eg titled WHAT WE DO
i dont want too much written on there or will look crowded, but options to add to back, from most important to least, please pick however many you think will look the best
new homes/extentions
led lighting and downlights
Solar Power
power
safety switches
switchboards
telephone and tv
smoke alarms
stoves and ovens
hot water systems
fault finding
re wiring
Updates

Thank you to those who have submitted designs, I would like to change my slogan to something more simple, I'm thinking something like. RELIABLE. EFFICIENT. PROFESSIONAL. AFFORDABLE. in what ever order you thinks fits best. Thanks

Industry/Entity Type

Contractor

```html
<!DOCTYPE html>
<html lang="en">
<head>
<meta charset="utf-8">
<title>D.O.R.B Electrical Contractors – Business Card</title>
<link href="https://fonts.googleapis.com/css2?family=Roboto+Condensed:wght@400;700&display=swap" rel="stylesheet">
<style>
  :root {
    --page: #efefef;
    --green-deep: #1f7a16;
    --green-mid: #4fa81c;
    --green-light: #9fd31c;
    --lime: #c9e81e;
    --black: #0b0b0b;
    --white: #ffffff;
    --ink-dark: #1e2a0c;
  }
  * { box-sizing: border-box; margin: 0; padding: 0; }
  html, body {
    width: 1200px; height: 973px; overflow: hidden;
    background: var(--page);
    font-family: "Roboto Condensed", "Arial Narrow", sans-serif;
  }
  .canvas { position: relative; width: 1200px; height: 973px; }

  .card {
    position: absolute;
    width: 560px; height: 320px;
    overflow: hidden;
    box-shadow: 0 6px 18px rgba(0,0,0,0.18);
  }
  .card--back  { left: 30px;  top: 120px; }
  .card--front { left: 610px; top: 533px; }

  .card__photo {
    position: absolute; inset: 0;
  }
  .card--back .card__photo {
    background:
      radial-gradient(circle at 78% 30%, #f4ff6a 0, var(--lime) 8%, transparent 22%),
      radial-gradient(ellipse at 75% 55%, var(--green-light) 0, var(--green-mid) 45%, var(--green-deep) 100%);
  }
  .card--front .card__photo {
    background:
      radial-gradient(circle at 30% 55%, #f4ff6a 0, var(--lime) 8%, transparent 22%),
      radial-gradient(ellipse at 35% 50%, var(--green-light) 0, var(--green-mid) 50%, var(--green-deep) 100%);
  }

  .badge {
    position: absolute;
    border-radius: 50%;
    background: var(--black);
    color: var(--white);
    text-align: center;
    display: flex; flex-direction: column; align-items: center; justify-content: center;
  }
  .card--back .badge  { width: 300px; height: 300px; left: 40px; top: 20px; }
  .card--front .badge { width: 310px; height: 310px; left: 230px; top: 5px; }

  .brand__name {
    color: var(--lime);
    font-weight: 400;
    letter-spacing: 3px;
    line-height: 1;
  }
  .brand__sub {
    color: var(--lime);
    font-size: 12px;
    letter-spacing: 0.5px;
    margin-top: 2px;
  }
  .card--back .brand__name { font-size: 40px; }
  .card--front .brand__name { font-size: 52px; }
  .card--front .brand__sub { color: var(--white); font-weight: 700; font-size: 16px; }

  .divider {
    width: 230px; border-top: 1px dotted var(--lime);
    margin: 8px 0 8px;
  }
  .services { list-style: none; font-size: 16px; line-height: 1.3; }

  .person__name { font-weight: 700; font-size: 20px; }
  .person__role { font-size: 16px; margin: 2px 0 8px; }
  .contact { list-style: none; font-size: 16px; line-height: 1.35; margin-top: 8px; }
  .contact__item { display: flex; align-items: center; justify-content: center; gap: 6px; }
  .contact__icon { width: 14px; height: 14px; flex: none; }

  .slogan {
    position: absolute; left: 28px; top: 34px;
    width: 220px;
    color: var(--ink-dark);
    font-size: 15px; line-height: 1.25;
  }
</style>
</head>
<body>
<main class="canvas">

  <section class="card card--back" aria-label="Card back – services">
    <div class="card__photo" role="img" aria-label="Close-up photograph of a glowing light bulb filament on a green background"></div>
    <div class="badge">
      <div class="brand">
        <div class="brand__name">D.O.R.B</div>
        <div class="brand__sub">ELECTRICAL CONTRACTORS</div>
      </div>
      <div class="divider"></div>
      <ul class="services">
        <li>New Homes / extentions</li>
        <li>LED Lighting and Downlights</li>
        <li>Solar Power | Safety Switches</li>
        <li>Switchboards | Telephone and TV</li>
        <li>Smoke Alarms | Stoves and Ovens</li>
        <li>Hot Water Systems | Re Wiring</li>
        <li>Fault Finding</li>
      </ul>
    </div>
  </section>

  <section class="card card--front" aria-label="Card front – contact details">
    <div class="card__photo" role="img" aria-label="Close-up photograph of a glowing light bulb filament on a green background"></div>
    <p class="slogan">Where excellence meets integrity, and service comes with a smile.</p>
    <div class="badge">
      <div class="person__name">CORBIN HOLT</div>
      <div class="person__role">A CLASS ELECTRICIAN</div>
      <div class="brand">
        <div class="brand__name">D.O.R.B</div>
        <div class="brand__sub">ELECTRICAL CONTRACTORS</div>
      </div>
      <ul class="contact">
        <li class="contact__item">
          <svg class="contact__icon" viewBox="0 0 14 14" aria-hidden="true">
            <circle cx="7" cy="7" r="7" fill="#fff"/>
            <rect x="3" y="4.5" width="8" height="5" fill="none" stroke="#0b0b0b" stroke-width="1"/>
            <polyline points="3,4.5 7,7.5 11,4.5" fill="none" stroke="#0b0b0b" stroke-width="1"/>
          </svg>
          DORB.ELECTRICAL@VELTOMAIL.COM
        </li>
        <li class="contact__item">
          <svg class="contact__icon" viewBox="0 0 14 14" aria-hidden="true">
            <circle cx="7" cy="7" r="7" fill="#fff"/>
            <path d="M4.6 3.6 L5.9 3.4 L6.5 5.3 L5.6 6 Q6.3 7.6 8 8.4 L8.7 7.5 L10.6 8.1 L10.4 9.4 Q7.8 10.6 5.6 8.4 Q3.4 6.2 4.6 3.6 Z" fill="#0b0b0b"/>
          </svg>
          0431576204
        </li>
        <li class="contact__item">LICENSE NO: TRN517394</li>
      </ul>
    </div>
  </section>

</main>
</body>
</html>
```